個人で販売しております沖縄のお菓子のラベルデザインをお願いします。

島のおやつ 「黒糖むしぱん」は、蒸しパンのような保存料不使用で、お年寄りからお子さんまで安心してお召し上がられます。一口食べてほこっりし、懐かしい味わいです。

お店の名前の由来でもある、沖縄の葉「月桃」をイメージしほっこりする感じに作成して頂きたいです。素敵なロゴの作成お願いします。

個人事業所なので、何もかもがわからないことだらけですが、どうぞよろしくお願い致します。

黒糖むしぱんも添付しております。

提案されたものに、入れたいと思っていたものが全部入っていたことが選んだ理由です。
そして、安価の予算にも関わらず修正も何度も引き受けて頂き感謝です。
最終納品時にはお手数おかけしましたが、本当にありがとうございました。

提案して頂きましたランサーの皆さん、初めての依頼で手こずってしまって
当選結果が遅れたことをお詫び申しあげます。
そして、素敵な提案して頂きましたことに感謝いたします。
本当にありがとうございました。

```html
<!DOCTYPE html>
<html lang="ja">
<head>
<meta charset="UTF-8">
<title>黒糖むしぱん ラベル</title>
<link href="https://fonts.googleapis.com/css2?family=Shippori+Mincho+B1:wght@500;800&display=swap" rel="stylesheet">
<style>
  :root {
    --bg: #ecebe7;
    --paper: #ffffff;
    --ink: #1b1b1b;
    --frame: #2a2a2a;
    --accent-light: #f3c9c9;
    --accent: #e08a8a;
    --leaf-dark: #5f9a3c;
    --leaf-light: #a9cf72;
    --tab: #4e8a33;
    --tab-text: #ffffff;
  }
  * { margin: 0; padding: 0; box-sizing: border-box; }
  html, body {
    width: 745px; height: 1200px; overflow: hidden;
    background: var(--bg);
  }
  .canvas { position: relative; width: 745px; height: 1200px; }
  .label {
    position: absolute; left: 60px; top: 130px;
    width: 625px; height: 940px;
    background: var(--paper);
    border: 3px solid var(--frame);
    box-shadow: 0 0 0 8px var(--paper), 0 0 0 10px var(--frame);
    font-family: "Shippori Mincho B1", serif;
    color: var(--ink);
    overflow: hidden;
  }
  .cord-art {
    position: absolute; left: 0; top: 30px;
    width: 250px; height: 210px;
    background: linear-gradient(135deg, var(--accent-light), var(--accent));
    opacity: 0.55;
  }
  .tagline {
    position: absolute; right: 40px; top: 40px;
    writing-mode: vertical-rl;
    font-size: 27px; font-weight: 500; line-height: 1.6;
    letter-spacing: 0.08em;
  }
  .title {
    position: absolute; left: 285px; top: 210px;
    writing-mode: vertical-rl;
    font-size: 84px; font-weight: 800; line-height: 1;
    letter-spacing: 0.04em;
  }
  .shop-tab {
    position: absolute; left: 70px; top: 600px;
    width: 78px; height: 300px;
    background: var(--tab);
    border: 3px solid var(--paper);
    outline: 2px solid var(--tab);
    display: flex; align-items: center; justify-content: center;
  }
  .shop-name {
    writing-mode: vertical-rl;
    color: var(--tab-text);
    font-size: 32px; font-weight: 800; letter-spacing: 0.18em;
  }
  .leaf-art {
    position: absolute; right: 30px; bottom: 40px;
    width: 210px; height: 230px;
    background: linear-gradient(160deg, var(--leaf-light), var(--leaf-dark));
  }
</style>
</head>
<body>
<div class="canvas">
  <div class="label">
    <div class="cord-art" role="img" aria-label="紅白の水引飾り"></div>

    <p class="tagline">月桃の葉がほのかに香る<br>ふんわり蒸し菓子</p>

    <h1 class="title">黒糖むしぱん</h1>

    <div class="shop-tab"><span class="shop-name">月の葉工房</span></div>

    <div class="leaf-art" role="img" aria-label="月桃の葉のイラスト"></div>
  </div>
</div>
</body>
</html>
```